Real Estate Design Website

I would like to have a design for "real estate agent" website. It needs to be in a "Responsive" framework.

The design need to be suitable for different viewer from all around the world. It needs to be modern. It'd be great if there is a design for mobile and tovix/tablet (it's all under responsive framework). It needs to be easy to navigate and look modern

Target Market(s)

End user/Real estate buyers from different part of the world

Industry/Entity Type

Real Estate

Requirements
Must have
• It's for real estate agent website which is used to represent their brand/image but at the same time it also for their client which is real estate buyers
Should not have
• Should not be boring design/out of date

```html
<!DOCTYPE html>
<html lang="en">
<head>
<meta charset="utf-8">
<title>Larkmoor Homes – Real Estate</title>
<link href="https://fonts.googleapis.com/css2?family=Quattrocento:wght@400;700&family=Kreon:wght@700&family=Cabin:ital,wght@0,400;0,700;1,400&family=Arimo:ital,wght@0,400;0,700;1,400&display=swap" rel="stylesheet">
<style>
:root{
  --blue:#1f86b8;
  --blue-dark:#106a98;
  --blue-light:#2b9bd0;
  --orange:#ee7023;
  --orange-light:#f68d3d;
  --orange-dark:#d85d12;
  --ink:#3a3a3a;
  --grey-text:#8a8a8a;
  --rule:#e3e3e3;
  --footer:#2f2f2f;
  --footer-text:#a9a9a9;
  --white:#ffffff;
}
*{margin:0;padding:0;box-sizing:border-box}
html,body{width:882px;height:1200px;overflow:hidden;background:var(--white)}
body{position:relative;font-family:"Cabin",Arial,sans-serif;color:var(--ink)}
.abs{position:absolute}

/* hero */
.hero-photo{left:0;top:0;width:882px;height:479px;
  background:radial-gradient(ellipse at 30% 45%,#e9d3c0 0%,#c9d6df 40%,#dfe8ee 70%,#eef3f6 100%)}

/* header */
.topbar{left:0;top:0;width:882px;height:110px}
.social{top:21px;width:28px;height:28px;border:2px solid var(--white);border-radius:50%}
.brand{left:333px;top:58px;width:200px;text-align:center;color:var(--white);
  font-family:"Quattrocento",serif;font-size:17px;letter-spacing:1px}
.brand-mark{left:426px;top:36px;width:14px;height:14px;background:var(--white)}
.nav{top:19px;height:25px;font:700 11px "Arimo",Arial,sans-serif;line-height:25px;color:var(--white);letter-spacing:.3px}
.nav-home{left:611px;width:56px;text-align:center;background:linear-gradient(#f68a3c,#e36716);border-radius:2px}

/* search panel */
.finder{left:543px;top:130px;width:313px;height:307px;background:rgba(240,243,245,.93);
  border:1px solid #d2d8dc;border-radius:3px;box-shadow:0 1px 4px rgba(0,0,0,.25)}
.finder-tab{left:585px;top:130px;width:228px;height:41px;background:linear-gradient(#f68d3d,#e1620f);
  border-radius:0 0 4px 4px;color:var(--white);text-align:center;line-height:41px;
  font-family:"Kreon",serif;font-size:25px;letter-spacing:.5px}
.field{background:var(--white);border:1px solid #c9cfd3;border-radius:3px;color:#9a9a9a;font-size:14px;padding-left:8px}
.field-location{left:560px;top:183px;width:277px;height:35px;line-height:33px;color:#333;font-size:16px}
.select{height:35px;line-height:33px}
.select::after{content:"";position:absolute;right:8px;top:14px;border:5px solid transparent;border-top-color:#666}
.col-a{left:560px;width:132px}
.col-b{left:703px;width:132px}
.btn-search{left:622px;top:385px;width:154px;height:34px;line-height:34px;text-align:center;
  background:linear-gradient(#1f8dc2,#0e6a9a);color:var(--white);font-size:18px;border-radius:2px}

/* testimonial band */
.band{left:0;top:439px;width:882px;height:236px}
.band-title{left:0;top:476px;width:870px;text-align:center;color:var(--white);font-family:"Quattrocento",serif;font-size:33px}
.arrow-btn{top:558px;width:46px;height:46px;border-radius:50%;background:var(--orange-light);border:2px solid #b64c0c}
.avatar{left:88px;top:531px;width:88px;height:88px;border-radius:50%;border:3px solid var(--white);
  background:radial-gradient(circle at 50% 40%,#f0d5bd,#c9a98a 70%,#9e8c7a)}
.quote-name{left:198px;top:533px;color:var(--white);font:15px "Arimo",Arial,sans-serif}
.quote-name b{font-style:italic;font-size:16px}
.quote{left:198px;top:562px;width:590px;color:var(--white);font:italic 15px/22px "Arimo",Arial,sans-serif;letter-spacing:-.2px}

/* offer section */
.offer-title{left:39px;top:700px;color:var(--orange);font-family:"Quattrocento",serif;font-size:35px}
.rule{left:39px;top:753px;width:554px;height:1px;background:var(--rule)}
.badge{top:776px;width:48px;height:48px;border-radius:50%;background:var(--blue);color:var(--white);
  text-align:center;line-height:48px;font-size:28px}
.offer-name{top:788px;font-size:18px;color:#333}
.offer-text{top:836px;width:160px;font:italic 11.3px/16.7px "Cabin",sans-serif;letter-spacing:.4px;color:var(--grey-text)}
.read-more{top:949px;font-size:11.5px;color:var(--orange);text-decoration:underline}
.read-more::after{content:"›";color:#555;margin-left:8px;display:inline-block}

/* stats card */
.stats{left:633px;top:731px;width:215px;height:239px;border-radius:6px;overflow:hidden;background:var(--blue)}
.stats-head{left:0;top:0;width:215px;height:40px;background:linear-gradient(var(--orange-light),var(--orange-dark));
  font:700 21px "Arimo",Arial,sans-serif;color:var(--white);padding:9px 0 0 16px;letter-spacing:-.3px}
.stats-head span{color:#222}
.stats-map{left:0;top:40px;width:215px;height:143px;background:linear-gradient(135deg,#dfeec4,#f1f3dd 50%,#cfe6b0)}
.stats-foot{left:0;top:183px;width:215px;height:56px;background:linear-gradient(#2a95c8,#0f6e9e)}
.stats-go{left:16px;top:15px;width:31px;height:31px;border-radius:50%;background:var(--orange)}
.stats-cta{left:58px;top:15px;color:var(--white);font:14px/16px "Arimo",Arial,sans-serif}

/* footer */
.footer{left:0;top:995px;width:882px;height:205px;background:var(--footer)}
.f-head{top:1030px;color:var(--white);font:700 15px "Arimo",Arial,sans-serif;letter-spacing:.3px}
.f-rule{top:1053px;height:1px;background:#555}
.f-links{top:1060px;color:var(--footer-text);font-size:12.3px;line-height:24px;letter-spacing:.8px;list-style:none}
.f-input{left:475px;top:1072px;width:177px;height:24px;border:1px solid #444;background:#262626;
  color:#999;font-size:12px;padding-left:8px;line-height:22px;letter-spacing:.6px}
.f-subscribe{left:585px;top:1110px;width:67px;height:23px;background:#000;color:var(--white);font-size:13px;text-align:center;line-height:23px;border-radius:2px}
.f-visit{left:713px;top:1044px;width:101px;height:32px;background:linear-gradient(#f68d3d,#dd5f10);
  color:var(--white);font-size:14px;text-align:center;line-height:32px;border-radius:2px}
.f-or{left:713px;top:1082px;width:101px;text-align:center;color:var(--footer-text);font-size:13px;letter-spacing:.5px}
.f-phone{left:700px;top:1100px;width:128px;text-align:center;color:var(--white);font:700 13px "Arimo",Arial,sans-serif}
</style>
</head>
<body>

<div class="abs hero-photo" role="img" aria-label="Photograph of a smiling young couple holding up the keys to their new home"></div>

<svg class="abs topbar" width="882" height="110" viewBox="0 0 882 110" aria-hidden="true">
  <defs>
    <linearGradient id="barGrad" x1="0" y1="0" x2="0" y2="1">
      <stop offset="0" stop-color="#2493c8"/><stop offset="1" stop-color="#136f9f"/>
    </linearGradient>
  </defs>
  <path d="M0 0H882V70H580L433 110L290 70H0Z" fill="url(#barGrad)"/>
</svg>

<div class="abs social" style="left:14px"></div>
<div class="abs social" style="left:51px"></div>
<div class="abs social" style="left:91px"></div>
<div class="abs social" style="left:131px"></div>

<div class="abs brand-mark"></div>
<div class="abs brand">Larkmoor Homes</div>

<div class="abs nav nav-home">HOME</div>
<div class="abs nav" style="left:684px">ABOUT</div>
<div class="abs nav" style="left:750px">RENT</div>
<div class="abs nav" style="left:807px">CONTACT</div>

<div class="abs finder"></div>
<div class="abs finder-tab">Find a Home</div>
<div class="abs field field-location">New York, NY</div>
<div class="abs field select col-a" style="top:229px">Beds</div>
<div class="abs field select col-b" style="top:229px">Baths</div>
<div class="abs field select col-a" style="top:280px">$ MIN</div>
<div class="abs field select col-b" style="top:280px">$ MAX</div>
<div class="abs field select col-a" style="top:332px">Sqft</div>
<div class="abs field select col-b" style="top:332px">Property Type</div>
<div class="abs btn-search">Search</div>

<svg class="abs band" width="882" height="236" viewBox="0 0 882 236" aria-hidden="true">
  <defs>
    <linearGradient id="bandGrad" x1="0" y1="0" x2="0" y2="1">
      <stop offset="0" stop-color="#f58530"/><stop offset="1" stop-color="#d85a10"/>
    </linearGradient>
  </defs>
  <path d="M0 40H290L432 0L580 40H882V236H0Z" fill="url(#bandGrad)"/>
</svg>
<div class="abs band-title">Recomendation</div>

<div class="abs arrow-btn" style="left:13px"></div>
<svg class="abs" style="left:27px;top:569px" width="18" height="24" viewBox="0 0 18 24" aria-hidden="true"><path d="M12 3L5 12L12 21" stroke="#fff" stroke-width="2" fill="none"/></svg>
<div class="abs arrow-btn" style="left:807px"></div>
<svg class="abs" style="left:823px;top:569px" width="18" height="24" viewBox="0 0 18 24" aria-hidden="true"><path d="M6 3L13 12L6 21" stroke="#fff" stroke-width="2" fill="none"/></svg>

<div class="abs avatar" role="img" aria-label="Portrait photo of the client giving the recommendation"></div>
<div class="abs quote-name"><b>Lena Varso</b> - CEO &amp; Co-founder at Real estate</div>
<p class="abs quote">Lorem ipsum dolor sit amet, consectetur adipisicing elit, sed do eiusmod tempor incididunt ut labore et dolore magna aliqua. Ut enim ad minim veniam, quis nostrud exercitation ullamco laboris nisi ut aliquip ex ea commodo consequat. Duis aute irure dolor in reprehenderit in voluptate velit esse cillum dolore eu fugiat nulla pariatur.</p>

<h2 class="abs offer-title">What we Offer</h2>
<div class="abs rule"></div>

<div class="abs badge" style="left:39px">A</div>
<div class="abs offer-name" style="left:97px">Appartments</div>
<p class="abs offer-text" style="left:39px">Lorem ipsum dolor sit amet, consectetur adipisicing elit, sed do eiusmod tempor incididunt ut labore et dolore magna aliqua. Ut enim ad minim veniam, quis nostrud...</p>
<a class="abs read-more" style="left:39px">Read More</a>

<div class="abs badge" style="left:224px">B</div>
<div class="abs offer-name" style="left:279px">Real estate</div>
<p class="abs offer-text" style="left:249px">Sed ut perspiciatis unde omnis iste natus error sit voluptatem accusantium doloremque laudantium, totam rem aperiam, eaque ipsa quae ab illo inventore veritatis...</p>
<a class="abs read-more" style="left:249px">Read More</a>

<div class="abs badge" style="left:409px">C</div>
<div class="abs offer-name" style="left:465px">Local Listnings</div>
<p class="abs offer-text" style="left:460px">At vero eos et accusamus et iusto odio dignissimos ducimus qui blanditiis praesentium voluptatum deleniti atque corrupti quos dolores et quas molestias excepturi...</p>
<a class="abs read-more" style="left:460px">Read More</a>

<div class="abs stats">
  <div class="abs stats-head">Live <span>Search Stats</span></div>
  <div class="abs stats-map" role="img" aria-label="Illustrated city map with green house location pins"></div>
  <div class="abs stats-foot">
    <div class="abs stats-go"></div>
    <svg class="abs" style="left:25px;top:23px" width="14" height="16" viewBox="0 0 14 16" aria-hidden="true"><path d="M4 2L10 8L4 14" stroke="#fff" stroke-width="3" fill="none"/></svg>
    <div class="abs stats-cta">Who's looking where?<br>Find out now</div>
  </div>
</div>

<footer class="abs footer"></footer>
<div class="abs f-head" style="left:38px">SITEMAP</div>
<div class="abs f-rule" style="left:38px;width:175px"></div>
<ul class="abs f-links" style="left:38px"><li>Home</li><li>About</li><li>Blog</li><li>Examples</li><li>Testimonials</li></ul>
<ul class="abs f-links" style="left:123px"><li>Privacy</li><li>Terms &amp; Condition</li><li>Terms of Services</li><li>Non-disclosure</li><li>Affiliate Programe</li></ul>

<div class="abs f-head" style="left:268px">SUPPORT &amp; CONTACT</div>
<div class="abs f-rule" style="left:268px;width:175px"></div>
<ul class="abs f-links" style="left:269px"><li>Client area</li><li>contact us</li><li>online chat</li><li>FAQ</li></ul>
<ul class="abs f-links" style="left:350px"><li>Chirper</li><li>Friendbook</li><li>Linkwork</li><li>Viewtube</li></ul>

<div class="abs f-head" style="left:474px">NEWSLETTER:</div>
<div class="abs f-rule" style="left:474px;width:175px"></div>
<div class="abs f-input">Enter your email here</div>
<div class="abs f-subscribe">Subscribe</div>

<div class="abs f-visit">Visit Now</div>
<div class="abs f-or">OR CALL</div>
<div class="abs f-phone">000 555 000 7777</div>

</body>
</html>
```